Business Cards and Stationary for Studio Calmaris (Massage Therapy)
BC for Massage Therapy Studio
Professional
Corwin Palde
President/CEO
742 Fenwick Rd.
Ste. 7C
Greer, SC 48213
cpalde@studiocalmaris.example
www.studiocalmaris.example
Logo AI file

```html
<!DOCTYPE html>
<html lang="en">
<head>
<meta charset="utf-8">
<title>Studio Calmaris – Stationery Set</title>
<link href="https://fonts.googleapis.com/css2?family=Montserrat:wght@400;600&display=swap" rel="stylesheet">
<style>
:root{
  --board:#3b3b3b;
  --board-dark:#2f2f2f;
  --paper:#ffffff;
  --ink:#3a3a3a;
  --muted:#8a8a8a;
  --gold:#d6c41c;
  --gold-deep:#a8970f;
  --charcoal:#262626;
  --faint:#ece9cf;
  --label:#b9b9b9;
}
*{margin:0;padding:0;box-sizing:border-box}
html,body{width:1200px;height:338px;overflow:hidden}
body{background:radial-gradient(ellipse at 50% 40%,var(--board) 0%,var(--board-dark) 100%);font-family:"Montserrat",Arial,sans-serif;position:relative;color:var(--ink)}
.piece{position:absolute;box-shadow:0 2px 6px rgba(0,0,0,.45)}
.label{position:absolute;font-size:5px;color:var(--label);letter-spacing:.3px}
.brand{display:flex;align-items:center;gap:3px}
.brand .dot{border-radius:50%;background:var(--gold);flex:none}
.brand .name{font-weight:600;color:var(--ink);white-space:nowrap}
.on-dark .name{color:var(--paper)}
.mark-faint{position:absolute;border-radius:50%;border:6px solid var(--faint);background:rgba(236,233,207,.35)}
.footer{position:absolute;font-size:3.6px;color:var(--muted);line-height:1.5}

/* business cards */
.card{width:110px;height:44px}
.card.dark{background:var(--charcoal)}
.card.light{background:var(--paper)}
/* letterheads */
.letterhead{width:218px;height:295px;background:var(--paper);top:24px}
/* envelopes */
.envelope{width:214px;height:86px;background:var(--paper);left:631px}
.env-back{left:888px;width:300px;overflow:hidden}
.flap{position:absolute;left:0;top:0;width:100%;height:100%}
</style>
</head>
<body>

<!-- business cards -->
<div class="label" style="left:12px;top:131px">Business Card Front</div>
<div class="piece card dark on-dark" style="left:12px;top:140px">
  <div class="brand" style="position:absolute;left:8px;top:10px">
    <span class="dot" style="width:8px;height:8px"></span>
    <span class="name" style="font-size:4.5px">Studio Calmaris</span>
  </div>
</div>
<div class="label" style="left:12px;top:192px">Business Card Back</div>
<div class="piece card dark on-dark" style="left:12px;top:201px">
  <div class="brand" style="position:absolute;left:34px;top:18px">
    <span class="dot" style="width:7px;height:7px"></span>
    <span class="name" style="font-size:4.5px">Studio Calmaris</span>
  </div>
</div>
<div class="piece card light" style="left:12px;top:262px;height:56px">
  <span style="position:absolute;left:8px;top:12px;width:4px;height:4px;border-radius:50%;background:var(--gold)"></span>
  <div class="footer" style="left:15px;top:8px">Corwin Palde<br>President/CEO<br>742 Fenwick Rd.<br>Ste. 7C<br>Greer, SC 48213<br>cpalde@studiocalmaris.example</div>
</div>

<!-- letterhead 1 -->
<div class="piece letterhead" style="left:137px">
  <div class="brand" style="position:absolute;left:14px;top:14px">
    <span class="dot" style="width:9px;height:9px"></span>
    <span class="name" style="font-size:4.5px">Studio Calmaris</span>
  </div>
  <div class="mark-faint" style="width:76px;height:76px;left:71px;top:112px"></div>
  <div class="footer" style="left:14px;top:252px">742 Fenwick Rd.<br>Ste. 7C<br>Greer, SC 48213<br>www.studiocalmaris.example</div>
</div>
<div class="label" style="left:215px;top:322px">Letterhead Version 1</div>

<!-- letterhead 2 -->
<div class="piece letterhead" style="left:384px">
  <div class="brand" style="position:absolute;left:72px;top:14px;flex-direction:column;gap:2px">
    <span class="dot" style="width:10px;height:10px"></span>
    <span class="name" style="font-size:4.5px">Studio Calmaris</span>
  </div>
  <div class="mark-faint" style="width:76px;height:76px;left:71px;top:112px"></div>
  <div class="footer" style="left:0;width:100%;text-align:center;top:280px">742 Fenwick Rd. Ste. 7C, Greer, SC 48213 · www.studiocalmaris.example</div>
</div>
<div class="label" style="left:460px;top:322px">Letterhead Version 2</div>

<!-- envelope fronts -->
<div class="piece envelope" style="top:106px">
  <div class="brand" style="position:absolute;left:10px;top:10px">
    <span class="dot" style="width:9px;height:9px"></span>
    <span class="name" style="font-size:4.5px">Studio Calmaris</span>
  </div>
</div>
<div class="label" style="left:715px;top:196px">Envelope Front</div>
<div class="piece envelope" style="top:235px;overflow:hidden">
  <div class="brand" style="position:absolute;left:10px;top:10px">
    <span class="dot" style="width:9px;height:9px"></span>
    <span class="name" style="font-size:4.5px">Studio Calmaris</span>
  </div>
  <div class="mark-faint" style="width:60px;height:60px;left:146px;top:16px;border-width:5px"></div>
</div>
<div class="label" style="left:715px;top:325px">Envelope Front</div>

<!-- envelope backs -->
<div class="piece env-back" style="top:24px;height:84px">
  <svg class="flap" viewBox="0 0 300 84" preserveAspectRatio="none">
    <defs><linearGradient id="goldFlap" x1="0" y1="0" x2="0" y2="1">
      <stop offset="0" stop-color="#e8d63a"/><stop offset="1" stop-color="#a8970f"/></linearGradient></defs>
    <rect width="300" height="84" fill="url(#goldFlap)"/>
    <path d="M0 0 L150 70 L300 0" fill="none" stroke="#8e800c" stroke-width="1"/>
  </svg>
</div>
<div class="piece env-back on-dark" style="top:108px;height:106px;background:var(--charcoal)">
  <svg class="flap" viewBox="0 0 300 106" preserveAspectRatio="none">
    <path d="M0 0 L150 40 L300 0 Z" fill="#333"/>
    <path d="M0 0 L150 40 L300 0" fill="none" stroke="#4a4a4a" stroke-width="1"/>
  </svg>
  <span style="position:absolute;left:144px;top:34px;width:12px;height:12px;border-radius:50%;background:var(--gold)"></span>
</div>
<div class="piece env-back" style="top:220px;height:102px;background:var(--paper)">
  <svg class="flap" viewBox="0 0 300 102" preserveAspectRatio="none">
    <path d="M0 0 L150 50 L300 0" fill="none" stroke="#cfcfcf" stroke-width="1"/>
    <path d="M0 102 L110 45 M300 102 L190 45" fill="none" stroke="#e2e2e2" stroke-width="1"/>
  </svg>
</div>
<div class="label" style="left:1010px;top:326px">Envelope Back Views</div>

</body>
</html>
```